out of the box Business Card Design for a Manufacturer / Distributor

We are a manufarturer and distributor of products.
the company name is VORTANI (Pic attached)

the picture is NOT a must have on the business Card.

the Business Card should look really professional and/or special, so out of the box thinking is welcome.

there should be 2 Adresses on the Business Card for Main and Branch Office.
Email Adress, homepage, Name is required
NO Phone Number

Our working field:
Private Labeling
high Quality Production
direct distribution
warehousing
trademark registration
legal support

Main Office:
Kornblumenweg 14
08352 Talbrück
Germany

Branch Office:
Daska Lane
Nurabad
Pakistan

Names:
Lukas Feldhaus (Owner)
Imran Qureshi (Owner)

Email:
lukas@vortani-example.com
imran@vortani-example.com

homepage:
vortani-example.com

Industry/Entity Type

Manufacturer Distributer

Contact Information for Business Card

Vortani

Requirements
Must have
• Names, both office Adresses, email, homepage
Should not have
• Phone Number

```html
<!DOCTYPE html>
<html lang="en">
<head>
<meta charset="utf-8">
<title>Vortani – Business Card</title>
<link rel="stylesheet" href="https://fonts.googleapis.com/css2?family=Montserrat:wght@300;400;500;600;700&display=swap">
<style>
  :root {
    --red: #f21d22;
    --red-bright: #fa2a1c;
    --crimson: #d4143a;
    --plum: #8a0b4c;
    --owner-panel: rgba(150, 12, 62, 0.42);
    --white: #ffffff;
    --white-soft: rgba(255, 255, 255, 0.85);
  }
  * { margin: 0; padding: 0; box-sizing: border-box; }
  html, body {
    width: 1200px; height: 686px; overflow: hidden;
    background: #ffffff;
  }
  .card {
    position: relative;
    width: 1200px; height: 686px; overflow: hidden;
    font-family: "Montserrat", sans-serif;
    color: var(--white);
    background:
      radial-gradient(ellipse 900px 520px at 0% 100%, var(--plum) 0%, rgba(138,11,76,0) 70%),
      linear-gradient(160deg, var(--red-bright) 0%, var(--red) 45%, var(--crimson) 100%);
  }
  .owner-panel {
    position: absolute;
    left: 800px; top: 97px; right: 0; height: 246px;
    background: var(--owner-panel);
    border-radius: 40px 0 0 246px;
  }
  .brand {
    position: absolute; left: 66px; top: 86px;
    display: flex; align-items: center; gap: 34px;
  }
  .brand-dot {
    width: 120px; height: 120px; border-radius: 50%;
    background: var(--white);
  }
  .brand-name {
    font-size: 88px; font-weight: 600; letter-spacing: 2px; line-height: 1;
  }
  .owner-label {
    position: absolute; left: 912px; top: 124px;
    display: flex; flex-direction: column; align-items: center;
    font-size: 26px; font-weight: 300; line-height: 35px;
  }
  .owner-colon {
    position: absolute; left: 937px; top: 194px;
    font-size: 26px; font-weight: 300; line-height: 35px;
  }
  .owner-names {
    position: absolute; left: 958px; top: 116px; width: 216px;
    text-align: center;
    font-size: 33px; font-weight: 600; line-height: 35px; letter-spacing: 1px;
  }
  .heading {
    position: absolute;
    font-size: 34px; font-weight: 600; letter-spacing: 2.5px; line-height: 1;
  }
  .services-heading { left: 65px; top: 278px; }
  .service-list {
    position: absolute; left: 65px; top: 321px; list-style: none;
  }
  .service-list li {
    display: block; width: max-content;
    font-size: 20px; font-weight: 500; letter-spacing: 1px;
    line-height: 24px; margin-bottom: 9px;
    border-bottom: 1px solid var(--white-soft);
  }
  .main-heading { left: 475px; top: 278px; }
  .branch-heading { left: 475px; top: 408px; }
  .address {
    position: absolute; left: 479px;
    font-style: normal;
    font-size: 19px; font-weight: 500; letter-spacing: 1px; line-height: 24px;
  }
  .main-address { top: 316px; }
  .branch-address { top: 447px; }
  .contact-heading {
    left: 65px; top: 562px; font-size: 24px; letter-spacing: 1.5px;
  }
  .contact-list {
    position: absolute; left: 65px; top: 593px;
    font-size: 17px; font-weight: 400; line-height: 23px; letter-spacing: 0.3px;
  }
  .footer-rule {
    position: absolute; left: 326px; top: 634px; width: 830px; height: 1px;
    background: var(--white-soft);
  }
  .website {
    position: absolute; left: 326px; width: 830px; top: 645px;
    text-align: center;
    font-size: 24px; font-weight: 400; letter-spacing: 2px;
  }
</style>
</head>
<body>
  <main class="card">
    <div class="owner-panel"></div>

    <div class="brand">
      <span class="brand-dot"></span>
      <span class="brand-name">VORTANI</span>
    </div>

    <div class="owner-label" aria-label="Owner:">
      <span>O</span><span>W</span><span>N</span><span>E</span><span>R</span>
    </div>
    <span class="owner-colon" aria-hidden="true">:</span>
    <div class="owner-names">
      LUKAS<br>FELDHAUS<br>&amp;<br>IMRAN<br>QURESHI
    </div>

    <h2 class="heading services-heading">OUR SERVICES</h2>
    <ul class="service-list">
      <li>PRIVATE LABELING</li>
      <li>HIGH QUALITY PRODUCTION</li>
      <li>DIRECT DISTRIBUTION</li>
      <li>WAREHOUSING</li>
      <li>TRADEMARK REGISTRATION</li>
      <li>LEGAL SUPPORT</li>
    </ul>

    <h2 class="heading main-heading">MAIN OFFICE:</h2>
    <address class="address main-address">
      KORNBLUMENWEG 14<br>08352 TALBRÜCK<br>GERMANY
    </address>

    <h2 class="heading branch-heading">BRANCH OFFICE:</h2>
    <address class="address branch-address">
      DASKA LANE<br>NURABAD<br>PAKISTAN
    </address>

    <h2 class="heading contact-heading">CONTACT US</h2>
    <div class="contact-list">
      lukas@vortani-example.com<br>imran@vortani-example.com
    </div>

    <div class="footer-rule"></div>
    <div class="website">VORTANI-EXAMPLE.COM</div>
  </main>
</body>
</html>
```